Meridel Hair Studio Needs a new appointment business card

We need a new appointment card for our hair salon.

I Dont want bright out there colours.
I would like it to be neat, clean, easy to read. White, Black, with a hint of colour if needed.

We need
-Logo
-Phone number 47208613
-Mobile Number: 0417306852
Address: Shop 3/214 Calder Road, The Elmgates, Mackay 4740

BACK SIDE OF CARD
- Appointment Time & Date (White background so we are able to write on it)
(If you are unable to make your appointment please contact us ASAP 47208613)

I also would like the chatterly and Pictorama logo(Find us on Chatterly)(find us on Pictorama)

Target Market(s)

appointment card simple to read. all information for their next appoint For all our clients male and female

Industry/Entity Type

Hairdresser

Contact Information for Business Card

-Logo
-Phone number 47208613

BACK SIDE OF CARD

Font styles to use
Serif
Sans Serif
Script

Requirements
Must have
• White Back ground on backside with appointment deatils so we are able to write information (like appointment time and date)
Nice to have
• Find us on Chatterly
and
pictorama - meridel_hairstudio
Should not have
• BRIGHT COLOURS

```html
<!DOCTYPE html>
<html lang="en">
<head>
<meta charset="utf-8">
<title>Meridel Hair Studio – Appointment Card</title>
<link rel="stylesheet" href="https://fonts.googleapis.com/css2?family=Poppins:wght@400;500;600;700&family=Lato:wght@400;700&display=swap">
<style>
  :root {
    --backdrop: #1e1e1f;
    --card: #f7f7f5;
    --ink: #141414;
    --rule: #222222;
    --accent: #1b9abd;
    --on-accent: #ffffff;
  }
  * { box-sizing: border-box; margin: 0; padding: 0; }
  html, body {
    width: 1200px; height: 960px; overflow: hidden;
    background: var(--backdrop);
  }
  .sheet {
    width: 1200px; height: 960px;
    display: flex; flex-direction: column; align-items: center; justify-content: center;
    gap: 30px;
  }
  .card {
    position: relative;
    width: 780px; height: 440px;
    background: var(--card);
    border-radius: 24px;
    overflow: hidden;
    color: var(--ink);
  }
  .wordmark {
    font-family: "Poppins", sans-serif;
    font-weight: 600;
    text-transform: uppercase;
    letter-spacing: 0.08em;
    color: var(--ink);
    white-space: nowrap;
  }

  /* Appointment side */
  .appointment .wordmark {
    position: absolute; top: 48px; right: 60px;
    font-size: 22px;
  }
  .appointment-title {
    position: absolute; top: 104px; left: 60px;
    font-family: "Poppins", sans-serif;
  }
  .appointment-title .main { display: block; font-size: 40px; font-weight: 700; line-height: 1; }
  .appointment-title .sub { display: block; font-size: 26px; font-weight: 600; line-height: 1.2; margin-left: 18px; }
  .fields {
    position: absolute; top: 200px; left: 90px; right: 60px;
    font-family: "Poppins", sans-serif; font-size: 22px;
    list-style: none;
  }
  .field { display: flex; align-items: flex-end; height: 46px; }
  .field-label { width: 92px; }
  .field-colon { width: 22px; }
  .field-line { flex: 1; border-bottom: 1.5px solid var(--rule); margin-bottom: 8px; }
  .notice {
    position: absolute; left: 90px; right: 40px; bottom: 40px;
    font-family: "Poppins", sans-serif; font-size: 15px;
    line-height: 1.3;
    white-space: nowrap;
  }

  /* Contact side */
  .contact .wave { position: absolute; inset: 0; width: 100%; height: 100%; }
  .contact .wordmark {
    position: absolute; left: 64px; top: 150px;
    font-size: 30px;
  }
  .divider {
    position: absolute; left: 434px; top: 70px;
    width: 2px; height: 170px; background: var(--rule);
  }
  .details {
    position: absolute; left: 460px; top: 76px;
    font-family: "Lato", sans-serif; font-size: 21px; line-height: 1.45;
    list-style: none;
  }
  .details li { display: flex; align-items: center; gap: 10px; white-space: nowrap; }
  .details .icon { width: 18px; height: 18px; flex: none; }
  .details .address { padding-left: 28px; }
  .social {
    position: absolute; right: 34px; bottom: 78px;
    display: flex; align-items: center; gap: 8px;
    font-family: "Lato", sans-serif; font-size: 20px; color: var(--on-accent);
  }
  .social .dot {
    width: 28px; height: 28px; border-radius: 50%;
    border: 2px solid var(--on-accent);
  }
</style>
</head>
<body>
<main class="sheet">

  <section class="card appointment" aria-label="Appointment reminder side">
    <div class="wordmark">Meridel Hair Studio</div>
    <h1 class="appointment-title">
      <span class="main">Appointment</span>
      <span class="sub">Reminder</span>
    </h1>
    <ul class="fields">
      <li class="field"><span class="field-label">Name</span><span class="field-colon">:</span><span class="field-line"></span></li>
      <li class="field"><span class="field-label">Date</span><span class="field-colon">:</span><span class="field-line"></span></li>
      <li class="field"><span class="field-label">Time</span><span class="field-colon">:</span><span class="field-line"></span></li>
    </ul>
    <p class="notice">If you are unable to make your appointment please contact us ASAP 47208613</p>
  </section>

  <section class="card contact" aria-label="Contact side">
    <svg class="wave" viewBox="0 0 780 440" preserveAspectRatio="none" aria-hidden="true">
      <path d="M0,402 C250,322 460,372 780,250 L780,440 L0,440 Z" fill="var(--accent)"/>
      <path d="M0,386 C250,306 460,356 780,236" fill="none" stroke="var(--ink)" stroke-width="7"/>
    </svg>

    <div class="wordmark">Meridel Hair Studio</div>
    <div class="divider"></div>

    <ul class="details">
      <li>
        <svg class="icon" viewBox="0 0 24 24" aria-hidden="true"><path d="M6.6 10.8a15 15 0 0 0 6.6 6.6l2.2-2.2a1 1 0 0 1 1-.25 11.4 11.4 0 0 0 3.6.57 1 1 0 0 1 1 1V20a1 1 0 0 1-1 1A17 17 0 0 1 3 4a1 1 0 0 1 1-1h3.5a1 1 0 0 1 1 1c0 1.250.2 2.450.57 3.6a1 1 0 0 1-.25 1z" fill="var(--accent)"/></svg>
        <span>47208613</span>
      </li>
      <li>
        <svg class="icon" viewBox="0 0 24 24" aria-hidden="true"><rect x="6" y="2" width="12" height="20" rx="2.5" fill="none" stroke="var(--accent)" stroke-width="2.2"/><circle cx="12" cy="18" r="1.2" fill="var(--accent)"/></svg>
        <span>0417306852</span>
      </li>
      <li class="address">Shop 3/214 Calder Road</li>
      <li class="address">The Elmgates, Mackay 4740</li>
    </ul>

    <div class="social">
      <span class="dot" aria-hidden="true"></span>
      <span class="dot" aria-hidden="true"></span>
      <span>meridel_hairstudio</span>
    </div>
  </section>

</main>
</body>
</html>
```